TV Antenna Installation business needs a unique flyer

We need a simple but effective flyer design for our TV Aerial installation company based in Newcastle, NSW, Australia called Clearpeak TV & Aerial Svcs.
We are trying to target areas where there has been a new transmitter installed and most houses just require their aerial redirecting and tv's retuning.

Industry/Entity Type

Business

Requirements
Must have
• We would like the idea of a headline phrase such as " Poor TV reception……..now a thing from the past" or something similar & catchy.
Also "Did you know a new transmitter has been recently installed in your area, we can therefore now GUARANTEE 100% PERFECT PICTURE
Charges from only $95.
- Free 5 year warranty
- Free signal testing
- Free Onsite Quote
Phone 0452 736 205
Nice to have
• Other services include:

- New Installs
- Extra Points & repairs
- TV wall mounting/Home Cinema
- Pull down tall masts

Modern tv picture, see example uploaded

```html
<!DOCTYPE html>
<html lang="en">
<head>
<meta charset="utf-8">
<title>Clearpeak TV &amp; Aerial Svcs – Flyer</title>
<link rel="stylesheet" href="https://fonts.googleapis.com/css2?family=Roboto+Condensed:wght@700&family=PT+Sans+Narrow:wght@400;700&display=swap">
<style>
  :root {
    --brand-blue: #1555a9;
    --deep-blue: #0d3f86;
    --red: #e2231f;
    --red-light: #ee5a57;
    --ink: #2f2f2f;
    --yellow: #ffe600;
    --paper: #ffffff;
    --mist: #eef2f6;
  }
  * { margin: 0; padding: 0; box-sizing: border-box; }
  html, body { width: 923px; height: 1200px; overflow: hidden; background: #f4f4f4; }
  .flyer {
    position: relative; width: 923px; height: 1200px; overflow: hidden;
    background: linear-gradient(180deg, var(--paper) 0%, var(--paper) 45%, var(--mist) 100%);
    font-family: "PT Sans Narrow", "Arial Narrow", sans-serif;
  }
  .business-name {
    position: absolute; top: 72px; left: 0; width: 100%;
    display: flex; justify-content: center; align-items: center; gap: 18px;
    font-family: "PT Sans Narrow", "Arial Narrow", sans-serif; font-weight: 700;
    color: var(--ink); font-size: 66px; line-height: 80px;
  }
  .business-name .mark { width: 26px; height: 26px; background: var(--red); flex: none; }
  .hero-band {
    position: absolute; top: 219px; left: 0; width: 100%; height: 330px;
    background: linear-gradient(90deg, var(--red) 0%, var(--red) 55%, var(--red-light) 100%);
  }
  .hero-band::after {
    content: ""; position: absolute; left: 0; right: 0; bottom: -40px; height: 40px;
    background: linear-gradient(180deg, rgba(226,35,31,0.25), rgba(226,35,31,0));
  }
  .location-tab {
    position: absolute; top: 219px; left: 242px; width: 420px; height: 34px;
    background: var(--paper); clip-path: polygon(0 0, 100% 0, 96% 100%, 4% 100%);
    font-family: "Roboto Condensed", sans-serif; font-weight: 700; font-size: 23px;
    color: var(--ink); text-align: center; line-height: 34px;
  }
  .headline {
    position: absolute; top: 270px; left: 45px; color: var(--paper);
    font-weight: 700; font-size: 50px; line-height: 60px;
    text-shadow: 0 2px 3px rgba(0,0,0,0.25);
  }
  .intro {
    position: absolute; top: 418px; left: 45px; width: 485px; color: var(--paper);
    font-size: 19px; line-height: 25px; text-align: justify;
  }
  .tv-illustration {
    position: absolute; top: 292px; left: 608px; width: 262px; height: 342px;
    border-radius: 40px 40px 20px 20px;
    background: radial-gradient(circle at 45% 45%, #fbeb6a 0%, #e8cc28 60%, #c9a915 100%);
  }
  .price-badge {
    position: absolute; top: 528px; left: 67px; width: 438px; height: 76px;
    background: linear-gradient(180deg, #2d78cf 0%, var(--brand-blue) 60%, var(--deep-blue) 100%);
    border-radius: 4px 4px 8px 8px; box-shadow: 0 4px 8px rgba(0,0,0,0.3);
    color: var(--paper); font-weight: 700; font-size: 40px; line-height: 76px; text-align: center;
  }
  .price-badge::before {
    content: ""; position: absolute; top: -9px; left: 0; width: 438px; height: 9px;
    background: #0a2f66; clip-path: polygon(3% 0, 97% 0, 100% 100%, 0 100%);
  }
  .call-line {
    position: absolute; top: 620px; left: 41px; display: flex; align-items: center; gap: 14px;
    font-family: "Roboto Condensed", sans-serif; font-weight: 700; color: var(--ink);
  }
  .call-line .label { font-size: 42px; color: #3a3a3a; }
  .call-line .number { font-size: 56px; letter-spacing: 1px; }
  .call-line svg { width: 92px; height: 64px; }
  .room-photo {
    position: absolute; top: 707px; left: 54px; width: 400px; height: 161px;
    border-radius: 12px; border: 3px solid #fff;
    box-shadow: 0 3px 10px rgba(0,0,0,0.3);
    background: linear-gradient(135deg, #e7c98e 0%, #c89b58 45%, #5b4a34 100%);
  }
  .transmitter-box {
    position: absolute; top: 888px; left: 54px; width: 398px; height: 270px;
    border-radius: 12px; border: 3px solid #fff;
    box-shadow: 0 3px 10px rgba(0,0,0,0.3);
    background: linear-gradient(180deg, #2f7cd3 0%, var(--brand-blue) 55%, #0e3d80 100%);
    text-align: center; padding-top: 20px;
  }
  .transmitter-box .note { color: var(--paper); font-weight: 700; font-size: 28px; line-height: 34px; }
  .transmitter-box .guarantee {
    margin-top: 14px; color: var(--yellow);
    font-family: "Roboto Condensed", sans-serif; font-weight: 700; font-size: 38px; line-height: 42px;
  }
  .services-title {
    position: absolute; top: 792px; left: 485px; color: var(--brand-blue);
    font-weight: 700; font-size: 32px;
  }
  .services-list { position: absolute; top: 840px; left: 497px; list-style: none; }
  .services-list li {
    display: flex; align-items: center; gap: 14px; height: 36.5px;
    font-size: 25px; color: var(--ink);
  }
  .services-list li::before {
    content: ""; width: 16px; height: 16px; border-radius: 50%;
    background: radial-gradient(circle at 35% 35%, #ff7a75, var(--red) 60%, #a8120f);
    box-shadow: 0 1px 3px rgba(0,0,0,0.35);
  }
  .perks-list { position: absolute; top: 1024px; left: 497px; list-style: none; }
  .perks-list li {
    display: flex; align-items: center; gap: 12px; height: 48px;
    font-weight: 700; font-size: 31px; color: var(--brand-blue);
  }
  .perks-list svg { width: 26px; height: 26px; }
</style>
</head>
<body>
<main class="flyer">
  <h1 class="business-name"><span class="mark" aria-hidden="true"></span>Clearpeak TV &amp; Aerial Svcs</h1>

  <section class="hero-band" aria-hidden="true"></section>
  <div class="location-tab">Newcastle, NSW, Australia</div>
  <h2 class="headline">Poor TV Reception?<br>Now a thing from the Past</h2>
  <p class="intro">We are trying to target areas where there has been a new transmitter installed and most houses just require their aerial redirecting and tv's retuning.</p>
  <div class="tv-illustration" role="img" aria-label="Illustration of a yellow retro television with antennas showing a signal line"></div>

  <div class="price-badge">Charges from only $95</div>

  <div class="call-line">
    <span class="label">Call:</span>
    <span class="number">0452 736 205</span>
    <svg viewBox="0 0 92 64" aria-hidden="true">
      <path d="M12 52 C28 64 70 62 88 50" fill="none" stroke="#888" stroke-width="2"/>
      <g transform="rotate(-30 40 32)">
        <rect x="18" y="4" width="22" height="14" rx="6" fill="#1a1a1a"/>
        <rect x="18" y="46" width="22" height="14" rx="6" fill="#1a1a1a"/>
        <rect x="18" y="10" width="9" height="44" rx="4" fill="#1a1a1a"/>
      </g>
    </svg>
  </div>

  <div class="room-photo" role="img" aria-label="Photo of a modern living room with a wall-mounted flat screen TV"></div>

  <section class="transmitter-box">
    <p class="note">Did you know a new<br>transmitter has been recently<br>installed in your area,<br>we can therefore NOW</p>
    <p class="guarantee">GUARANTEE 100%<br>PERFECT PICTURE</p>
  </section>

  <h3 class="services-title">OUR OTHER SERVICES:</h3>
  <ul class="services-list">
    <li>New Installs</li>
    <li>Extra Points &amp; repairs</li>
    <li>TV wall mounting/Home Cinema</li>
    <li>Pull down tall masts</li>
  </ul>

  <ul class="perks-list">
    <li><svg viewBox="0 0 26 26" aria-hidden="true"><rect x="1" y="5" width="18" height="18" rx="2" fill="none" stroke="#b01512" stroke-width="2"/><path d="M5 13 L10 19 L24 2" fill="none" stroke="#b01512" stroke-width="4" stroke-linecap="round" stroke-linejoin="round"/></svg>Free 5 Year Warranty</li>
    <li><svg viewBox="0 0 26 26" aria-hidden="true"><rect x="1" y="5" width="18" height="18" rx="2" fill="none" stroke="#b01512" stroke-width="2"/><path d="M5 13 L10 19 L24 2" fill="none" stroke="#b01512" stroke-width="4" stroke-linecap="round" stroke-linejoin="round"/></svg>Free Signal Testing</li>
    <li><svg viewBox="0 0 26 26" aria-hidden="true"><rect x="1" y="5" width="18" height="18" rx="2" fill="none" stroke="#b01512" stroke-width="2"/><path d="M5 13 L10 19 L24 2" fill="none" stroke="#b01512" stroke-width="4" stroke-linecap="round" stroke-linejoin="round"/></svg>Free Onsite Quote</li>
  </ul>
</main>
</body>
</html>
```